VELRO - Business cards

Business card to be created for Commercial sales staff

Target Market(s)

Commercial businesses

Industry/Entity Type

Commercial

Contact Information for Business Card

Look professional. For commercial clients

Colors
ffffff

Requirements
Must have
• - Velro Logo
• - Commercial sales staff as postion
• - room for commerical sales manager role
• - person name and their mobile number
• - Website : velropower.com.au
Nice to have
• White background.
• On back of business card just have the logo no other information
Should not have
• Should only have white background on front of card.

```html
<!DOCTYPE html>
<html lang="en">
<head>
<meta charset="utf-8">
<title>Velro – Business Cards</title>
<link rel="stylesheet" href="https://fonts.googleapis.com/css2?family=Source+Sans+3:ital,wght@0,400;0,600;0,700;0,800;1,400&display=swap">
<style>
  :root {
    --brand-red: #c4141b;
    --brand-charcoal: #31343c;
    --paper: #ffffff;
    --stage: #e8e6e3;
    --text-light: #ffffff;
    --font-main: "Source Sans 3", sans-serif;
  }
  * { box-sizing: border-box; margin: 0; padding: 0; }
  html, body {
    width: 1200px;
    height: 987px;
    overflow: hidden;
    background: var(--stage);
    font-family: var(--font-main);
  }
  .canvas {
    position: relative;
    width: 1200px;
    height: 987px;
  }
  .card {
    position: absolute;
    left: 293px;
    width: 615px;
    height: 349px;
    box-shadow: 0 2px 8px rgba(0,0,0,0.25);
  }
  .card--front { top: 131px; background: var(--paper); }
  .card--back  { top: 506px; background: var(--brand-charcoal); }

  .brand {
    position: absolute;
    left: 0;
    right: 0;
    display: flex;
    align-items: center;
    justify-content: center;
    gap: 14px;
  }
  .brand__dot {
    width: 34px;
    height: 34px;
    border-radius: 50%;
    background: var(--brand-red);
  }
  .brand__name {
    font-size: 72px;
    font-weight: 800;
    letter-spacing: 2px;
    line-height: 1;
  }
  .card--front .brand { top: 86px; }
  .card--front .brand__name { color: var(--brand-charcoal); }
  .card--back .brand { top: 120px; }
  .card--back .brand__name { color: var(--text-light); }

  .contact-bands {
    position: absolute;
    top: 241px;
    left: 0;
    width: 615px;
    height: 98px;
    display: flex;
    gap: 5px;
  }
  .band {
    height: 100%;
    color: var(--text-light);
  }
  .band--person {
    width: 306px;
    background: var(--brand-red);
    text-align: right;
    padding: 12px 25px 0 0;
  }
  .band--details {
    flex: 1;
    background: var(--brand-charcoal);
    padding: 11px 0 0 28px;
  }
  .person__name {
    font-size: 23px;
    font-weight: 600;
    letter-spacing: 0.5px;
    line-height: 27px;
  }
  .person__role,
  .person__email {
    font-size: 17px;
    font-weight: 400;
    line-height: 23px;
  }
  .details__line {
    font-size: 17px;
    line-height: 23px;
  }
  .details__label { font-weight: 600; }

  .back__web {
    position: absolute;
    top: 282px;
    left: 0;
    right: 0;
    text-align: center;
    color: var(--text-light);
    font-size: 17px;
    font-style: italic;
    letter-spacing: 2.5px;
  }
</style>
</head>
<body>
<main class="canvas">
  <section class="card card--front" aria-label="Business card front">
    <div class="brand">
      <span class="brand__dot"></span>
      <span class="brand__name">VELRO</span>
    </div>
    <div class="contact-bands">
      <div class="band band--person">
        <p class="person__name">DANIEL HART</p>
        <p class="person__role">Manager, Commerical Sales</p>
        <p class="person__email">daniel@velropower.com.au</p>
      </div>
      <div class="band band--details">
        <p class="details__line"><span class="details__label">(P)</span> 612 555 0184</p>
        <p class="details__line"><span class="details__label">(C)</span> 0412 555 937</p>
        <p class="details__line">www.velropower.com.au</p>
      </div>
    </div>
  </section>

  <section class="card card--back" aria-label="Business card back">
    <div class="brand">
      <span class="brand__dot"></span>
      <span class="brand__name">VELRO</span>
    </div>
    <p class="back__web">www.velropower.com.au</p>
  </section>
</main>
</body>
</html>
```